Bright Arrow Delivery Service Wordpress design

My client is a delivery service whose motto is "We carry it where you need it." Their colors are red, white and blue. They use Voyalo vans and box vans - NO semi tractors. They like this Website design www.tovamu-sample.com, but I would like to see some designs that make them stand out. Attached is their new logo.

Target Market(s)

Businesses who use delivery services in town and anyone needing freight picked up or transported in the United States.

Industry/Entity Type

Delivery Service

Number of Pages Required

1 page

Font styles to use
Sans Serif

Colors
ec1f27
0455a3
ffffff

Requirements
Must have
• We need a Wordpress design with sliders that incorporates their new logo and the motto "WE CARRY IT WHERE YOU NEED IT" Their corporate colors are red, white and blue. They only use voyalo vans and box vans.
Nice to have
• Please use your creativity to come up with a unique design for this delivery service.
Should not have
• NO SEMI TRACTOR TRAILERS

```html
<!DOCTYPE html>
<html lang="en">
<head>
<meta charset="utf-8">
<title>Bright Arrow Express Delivery</title>
<link href="https://fonts.googleapis.com/css2?family=Exo+2:wght@400;500;600;700&family=Open+Sans:wght@400;600;700&family=Roboto+Condensed:wght@400;700&display=swap" rel="stylesheet">
<style>
:root{
  --navy:#1d1866;
  --red:#ec1f27;
  --white:#ffffff;
  --light:#eeeeee;
  --text:#6a6a6a;
  --line:#c9c9d8;
}
*{margin:0;padding:0;box-sizing:border-box}
html,body{width:1200px;height:3015px;overflow:hidden}
body{position:relative;background:var(--white);font-family:"Open Sans",Arial,sans-serif;color:var(--text)}
.abs{position:absolute}
.heading{font-family:"Exo 2",Arial,sans-serif;font-weight:500;text-transform:uppercase;color:var(--navy);text-align:center;left:0;width:1200px}
.heading .accent{color:var(--red)}
.rule{height:6px;display:flex}
.rule span{flex:1}
.rule span:first-child{background:var(--navy)}
.rule span:last-child{background:var(--red)}
.photo{background:linear-gradient(160deg,#c8ccd2,#8f959e)}
.read-more{font-weight:700;font-size:15px;color:var(--red);text-transform:uppercase}
.read-more svg{vertical-align:middle;margin-left:4px}

/* top bar + header */
.topbar-left{left:0;top:0;width:560px;height:40px;background:var(--navy)}
.topbar-right{left:500px;top:0;width:700px;height:40px;background:var(--red);clip-path:polygon(40px 0,100% 0,100% 100%,0 100%)}
.social{top:13px;width:14px;height:14px;border-radius:50%;background:var(--white)}
.call-top{left:804px;top:5px;font-family:"Exo 2",sans-serif;font-style:italic;font-size:24px;color:var(--white);display:flex;align-items:center;gap:10px}
.header-bar{left:0;top:40px;width:1200px;height:110px;background:var(--navy)}
.brand-area{left:0;top:40px;width:580px;height:110px;background:var(--white);clip-path:polygon(0 0,500px 0,580px 100%,0 100%)}
.brand-name{left:84px;top:70px;font-family:"Exo 2",sans-serif;font-weight:700;font-size:38px;color:var(--navy);letter-spacing:1px}
.brand-mark{left:400px;top:62px;width:60px;height:60px;border-radius:50%;background:var(--navy)}
.nav{top:80px;font-family:"Exo 2",sans-serif;font-size:18px;color:#c8c7e0;text-transform:uppercase}
.nav-active{left:556px;top:70px;width:116px;height:44px;background:var(--red);clip-path:polygon(14px 0,100% 0,calc(100% - 14px) 100%,0 100%);color:var(--white);display:flex;align-items:center;justify-content:center}

/* hero */
.hero{left:0;top:150px;width:1200px;height:570px;background:linear-gradient(180deg,#6f9fcf 0%,#b7d0e4 38%,#8c9d55 55%,#5b5e48 75%,#3e3f3f 100%)}
.hero-tag{font-family:"Roboto Condensed",sans-serif;font-size:30px;color:var(--white);display:flex;align-items:center;justify-content:center;text-transform:uppercase}
.tag-express{left:720px;top:396px;width:214px;height:48px;background:var(--red);clip-path:polygon(0 0,100% 0,97% 100%,0 100%)}
.tag-delivery{left:924px;top:410px;width:232px;height:50px;background:var(--navy);clip-path:polygon(4% 0,100% 0,96% 100%,0 100%)}
.motto{left:716px;top:470px;width:440px;text-align:right;font-family:"Roboto Condensed",sans-serif;font-size:27px;color:var(--navy);text-transform:uppercase}

/* steps band */
.steps{left:0;top:720px;width:1200px;height:122px;background:var(--red)}
.step-icon{width:92px;height:92px;border-radius:50%;background:var(--navy);display:flex;align-items:center;justify-content:center;top:734px}
.step-title{top:736px;font-family:"Exo 2",sans-serif;font-size:32px;color:var(--white);text-transform:uppercase}
.step-text{top:776px;font-size:15px;line-height:24px;color:var(--white);width:200px}

/* welcome */
.welcome-text{left:180px;top:980px;width:840px;text-align:center;font-size:15px;line-height:26px}

/* services */
.services{left:0;top:1110px;width:1200px;height:362px;background:var(--light)}
.service-title{font-family:"Open Sans",sans-serif;font-size:20px;color:var(--navy);top:1262px}
.service-text{top:1296px;width:256px;font-size:15px;line-height:26px}

/* call band */
.call-navy{left:0;top:1472px;width:1200px;height:156px;background:var(--navy)}
.call-red{left:600px;top:1472px;width:600px;height:156px;background:var(--red);clip-path:polygon(60px 0,100% 0,100% 100%,0 100%)}
.call-label{left:78px;top:1532px;font-family:"Exo 2",sans-serif;font-size:27px;color:var(--white);text-transform:uppercase}
.call-phone{left:280px;top:1520px;width:60px;height:60px;border-radius:50%;background:var(--white);display:flex;align-items:center;justify-content:center}
.call-number{left:358px;top:1528px;font-family:"Exo 2",sans-serif;font-weight:600;font-size:30px;color:var(--white)}
.track-mark{left:584px;top:1514px;width:72px;height:72px;border-radius:50%;background:var(--white)}
.track-brand{left:720px;top:1486px;font-family:"Exo 2",sans-serif;font-weight:600;font-size:20px;color:var(--white);text-transform:uppercase}
.track-title{left:720px;top:1520px;font-family:"Exo 2",sans-serif;font-size:28px;color:var(--white);text-transform:uppercase}
.signup{left:728px;top:1564px;width:148px;height:44px;background:var(--navy);clip-path:polygon(10px 0,100% 0,calc(100% - 10px) 100%,0 100%);color:var(--white);font-family:"Exo 2",sans-serif;font-size:19px;display:flex;align-items:center;justify-content:center}

/* testimonial */
.testimonial{left:0;top:1628px;width:1200px;height:340px;background:var(--light)}
.quote-text{left:180px;top:1810px;width:840px;text-align:center;font-size:15px;line-height:26px}
.client{left:0;width:1200px;top:1888px;text-align:center;font-size:15px;font-weight:700;color:var(--red);text-transform:uppercase}
.arrow-btn{top:1810px;width:62px;height:62px;border-radius:50%;background:var(--navy);display:flex;align-items:center;justify-content:center}

/* news */
.news-img{top:2106px;width:234px;height:146px}
.news-title{top:2268px;font-size:17px;color:var(--navy)}
.news-date{top:2296px;font-size:13px;color:#8a8a8a;display:flex;align-items:center;gap:6px}
.news-text{top:2320px;width:262px;font-size:15px;line-height:25px}
.news-more{top:2398px}

/* footer */
.footer-shape{left:0;top:2360px}
.footer-mark{left:554px;top:2544px;width:72px;height:72px;border-radius:50%;background:var(--white)}
.foot-heading{top:2648px;font-family:"Open Sans",sans-serif;font-size:20px;color:var(--white);text-transform:uppercase}
.foot-divider{left:597px;top:2640px;width:2px;height:270px;background:#5a57a0}
.city{left:80px;font-size:16px;color:var(--white)}
.city-phone{left:284px;font-size:16px;color:var(--white);display:flex;align-items:center;gap:8px}
.field{border:2px solid #c8c7e6;color:var(--white);font-size:15px;padding:6px 8px}
.submit{left:650px;top:2874px;width:122px;height:36px;background:var(--red);color:var(--white);font-family:"Exo 2",sans-serif;font-size:19px;display:flex;align-items:center;justify-content:center}
.copyright{left:0;top:2945px;width:1200px;height:70px;background:var(--red);color:var(--white);font-size:15px;display:flex;align-items:center;justify-content:center}
</style>
</head>
<body>

<!-- top bar -->
<div class="abs topbar-left"></div>
<div class="abs topbar-right"></div>
<span class="abs social" style="left:74px"></span>
<span class="abs social" style="left:120px"></span>
<span class="abs social" style="left:168px"></span>
<div class="abs call-top">CALL US NOW
  <svg width="22" height="22" viewBox="0 0 24 24"><path fill="#fff" d="M6.6 10.8a15.1 15.1 0 0 0 6.6 6.6l2.2-2.2c.3-.3.7-.4 1-.2 1.1.4 2.3.6 3.6.6.6 0 1 .4 1 1V20c0 .6-.4 1-1 1A17 17 0 0 1 3 4c0-.6.4-1 1-1h3.5c.6 0 1 .4 1 1 0 1.3.2 2.5.6 3.6.1.3 0 .7-.2 1z"/></svg>
  <span style="font-style:normal;font-weight:600">123 456 7890</span></div>

<!-- header -->
<div class="abs header-bar"></div>
<div class="abs brand-area"></div>
<div class="abs brand-name">BRIGHT ARROW</div>
<div class="abs brand-mark"></div>
<div class="abs nav nav-active">Home</div>
<div class="abs nav" style="left:696px">About</div>
<div class="abs nav" style="left:794px">Services</div>
<div class="abs nav" style="left:922px">Career</div>
<div class="abs nav" style="left:1038px">Contact</div>

<!-- hero slider -->
<div class="abs hero" role="img" aria-label="Photo of a white delivery van driving along a country road at speed, trees and sky behind"></div>
<div class="abs hero-tag tag-express">Express</div>
<div class="abs hero-tag tag-delivery">Delivery</div>
<div class="abs motto">We carry it where you need it</div>

<!-- steps -->
<div class="abs steps"></div>
<div class="abs step-icon" style="left:74px">
  <svg width="42" height="38" viewBox="0 0 24 22"><path fill="#fff" d="M1 1h3.5l1 3H23l-2.5 9H7.2l.6 2H21v2H6.3L3 3H1z"/><circle cx="9" cy="19.5" r="1.8" fill="#fff"/><circle cx="18" cy="19.5" r="1.8" fill="#fff"/></svg>
</div>
<div class="abs step-title" style="left:184px">Order</div>
<div class="abs step-text" style="left:184px">Lorem Ipsum is simply dummy text of the printing.</div>

<div class="abs step-icon" style="left:444px">
  <svg width="46" height="46" viewBox="0 0 24 24"><circle cx="12" cy="12" r="10" fill="none" stroke="#fff" stroke-width="2.4"/><path d="M12 6v6h4" fill="none" stroke="#fff" stroke-width="2.4"/></svg>
</div>
<div class="abs step-title" style="left:550px">Wait</div>
<div class="abs step-text" style="left:550px">Lorem Ipsum is simply dummy text of the printing.</div>

<div class="abs step-icon" style="left:808px">
  <svg width="46" height="36" viewBox="0 0 26 20"><path fill="#fff" d="M1 2h14v12H1zM16 6h5l4 5v3h-9z"/><circle cx="6" cy="16" r="2.6" fill="#fff"/><circle cx="20" cy="16" r="2.6" fill="#fff"/></svg>
</div>
<div class="abs step-title" style="left:912px">Deliver</div>
<div class="abs step-text" style="left:912px">Lorem Ipsum is simply dummy text of the printing.</div>

<!-- welcome -->
<h1 class="abs heading" style="top:892px;font-size:44px"><span class="accent">Welcome to</span> Bright Arrow Express Delivery</h1>
<div class="abs rule" style="left:120px;top:950px;width:964px"><span></span><span></span></div>
<p class="abs welcome-text">Lorem Ipsum is simply dummy text of the printing and typesetting industry. Lorem Ipsum has been the industry's standard dummy text ever since the 1500s, when an unknown printer took a galley of type and scrambled it to make a type specimen book.</p>

<!-- services -->
<section class="abs services"></section>
<h2 class="abs heading" style="top:1162px;font-size:44px"><span class="accent">Services</span> we provide</h2>
<div class="abs rule" style="left:364px;top:1220px;width:466px"><span></span><span></span></div>

<div class="abs photo" style="left:76px;top:1262px;width:208px;height:138px" role="img" aria-label="Photo of a white Voyalo van"></div>
<div class="abs service-title" style="left:298px">Delivery By Voyalo Vans</div>
<p class="abs service-text" style="left:298px">Lorem Ipsum is simply dummy text of the printing and typesetting industry.</p>
<div class="abs read-more" style="left:298px;top:1374px">Read more<svg width="14" height="12" viewBox="0 0 14 12"><path d="M1 1l5 5-5 5M7 1l5 5-5 5" fill="none" stroke="#ec1f27" stroke-width="2.2"/></svg></div>

<div class="abs photo" style="left:632px;top:1262px;width:208px;height:138px" role="img" aria-label="Photo of a white box van"></div>
<div class="abs service-title" style="left:854px">Delivery By Box Vans</div>
<p class="abs service-text" style="left:854px">Lorem Ipsum is simply dummy text of the printing and typesetting industry.</p>
<div class="abs read-more" style="left:854px;top:1374px">Read more<svg width="14" height="12" viewBox="0 0 14 12"><path d="M1 1l5 5-5 5M7 1l5 5-5 5" fill="none" stroke="#ec1f27" stroke-width="2.2"/></svg></div>

<!-- call / tracking band -->
<div class="abs call-navy"></div>
<div class="abs call-red"></div>
<div class="abs call-label">Call us now</div>
<div class="abs call-phone"><svg width="28" height="28" viewBox="0 0 24 24"><path fill="#ec1f27" d="M6.6 10.8a15.1 15.1 0 0 0 6.6 6.6l2.2-2.2c.3-.3.7-.4 1-.2 1.1.4 2.3.6 3.6.6.6 0 1 .4 1 1V20c0 .6-.4 1-1 1A17 17 0 0 1 3 4c0-.6.4-1 1-1h3.5c.6 0 1 .4 1 1 0 1.3.2 2.5.6 3.6.1.3 0 .7-.2 1z"/></svg></div>
<div class="abs call-number">123 456 7890</div>
<div class="abs track-mark"></div>
<div class="abs track-brand">Bright Arrow Express Delivery</div>
<div class="abs track-title">Order &amp; Tracking System</div>
<div class="abs signup">SIGN UP</div>

<!-- testimonial -->
<section class="abs testimonial"></section>
<h2 class="abs heading" style="top:1670px;font-size:44px"><span class="accent">What our</span> client say</h2>
<div class="abs rule" style="left:364px;top:1728px;width:466px"><span></span><span></span></div>
<svg class="abs" style="left:582px;top:1760px" width="36" height="28" viewBox="0 0 36 28"><path fill="#333" d="M0 28V16C0 7 4 2 12 0l2 4C9 6 7 9 7 13h7v15zM20 28V16c0-9 4-14 12-16l2 4c-5 2-7 5-7 9h7v15z"/></svg>
<p class="abs quote-text">Lorem Ipsum is simply dummy text of the printing and typesetting industry. Lorem Ipsum has been the industry's standard dummy text ever since the 1500.</p>
<div class="abs client">- Client Name</div>
<div class="abs arrow-btn" style="left:82px"><svg width="18" height="30" viewBox="0 0 18 30"><path d="M15 2L3 15l12 13" fill="none" stroke="#fff" stroke-width="2.5"/></svg></div>
<div class="abs arrow-btn" style="left:1052px"><svg width="18" height="30" viewBox="0 0 18 30"><path d="M3 2l12 13L3 28" fill="none" stroke="#fff" stroke-width="2.5"/></svg></div>

<!-- latest news -->
<h2 class="abs heading" style="top:2008px;font-size:44px"><span class="accent">Latest</span> News</h2>
<div class="abs rule" style="left:454px;top:2066px;width:278px"><span></span><span></span></div>

<div class="abs photo news-img" style="left:76px" role="img" aria-label="Photo of a courier handing a parcel to a customer at her door"></div>
<div class="abs photo news-img" style="left:346px" role="img" aria-label="Photo of a courier carrying a parcel outside a building"></div>
<div class="abs photo news-img" style="left:616px" role="img" aria-label="Photo of a white delivery van parked on a street"></div>
<div class="abs photo news-img" style="left:886px" role="img" aria-label="Photo of a worker unloading boxes from the back of a van"></div>

<div class="abs news-title" style="left:78px">Lorem Ipsum is dummy text.</div>
<div class="abs news-title" style="left:348px">Lorem Ipsum is dummy text.</div>
<div class="abs news-title" style="left:618px">Lorem Ipsum is dummy text.</div>
<div class="abs news-title" style="left:888px">Lorem Ipsum is dummy text.</div>

<div class="abs news-date" style="left:78px"><svg width="12" height="12" viewBox="0 0 12 12"><rect x="1" y="2" width="10" height="9" fill="none" stroke="#8a8a8a"/><path d="M1 5h10" stroke="#8a8a8a"/></svg>17 June 2016</div>
<div class="abs news-date" style="left:348px"><svg width="12" height="12" viewBox="0 0 12 12"><rect x="1" y="2" width="10" height="9" fill="none" stroke="#8a8a8a"/><path d="M1 5h10" stroke="#8a8a8a"/></svg>17 June 2016</div>
<div class="abs news-date" style="left:618px"><svg width="12" height="12" viewBox="0 0 12 12"><rect x="1" y="2" width="10" height="9" fill="none" stroke="#8a8a8a"/><path d="M1 5h10" stroke="#8a8a8a"/></svg>17 June 2016</div>
<div class="abs news-date" style="left:888px"><svg width="12" height="12" viewBox="0 0 12 12"><rect x="1" y="2" width="10" height="9" fill="none" stroke="#8a8a8a"/><path d="M1 5h10" stroke="#8a8a8a"/></svg>17 June 2016</div>

<p class="abs news-text" style="left:78px">Lorem Ipsum is simply dummy text of the printing and typesetting industry.</p>
<p class="abs news-text" style="left:348px">Lorem Ipsum is simply dummy text of the printing and typesetting industry.</p>
<p class="abs news-text" style="left:618px">Lorem Ipsum is simply dummy text of the printing and typesetting industry.</p>
<p class="abs news-text" style="left:888px">Lorem Ipsum is simply dummy text of the printing and typesetting industry.</p>

<div class="abs read-more news-more" style="left:78px">Read more<svg width="14" height="12" viewBox="0 0 14 12"><path d="M1 1l5 5-5 5M7 1l5 5-5 5" fill="none" stroke="#ec1f27" stroke-width="2.2"/></svg></div>
<div class="abs read-more news-more" style="left:348px">Read more<svg width="14" height="12" viewBox="0 0 14 12"><path d="M1 1l5 5-5 5M7 1l5 5-5 5" fill="none" stroke="#ec1f27" stroke-width="2.2"/></svg></div>
<div class="abs read-more news-more" style="left:618px">Read more<svg width="14" height="12" viewBox="0 0 14 12"><path d="M1 1l5 5-5 5M7 1l5 5-5 5" fill="none" stroke="#ec1f27" stroke-width="2.2"/></svg></div>
<div class="abs read-more news-more" style="left:888px">Read more<svg width="14" height="12" viewBox="0 0 14 12"><path d="M1 1l5 5-5 5M7 1l5 5-5 5" fill="none" stroke="#ec1f27" stroke-width="2.2"/></svg></div>

<!-- footer -->
<svg class="abs footer-shape" width="1200" height="585" viewBox="0 2360 1200 585">
  <path d="M0 2610 Q600 2372 1200 2610 V2945 H0 Z" fill="#ec1f27"/>
  <path d="M0 2624 Q600 2390 1200 2624 V2945 H0 Z" fill="#1d1866"/>
</svg>
<div class="abs footer-mark"></div>

<div class="abs foot-heading" style="left:80px">New customer click for information</div>
<div class="abs foot-divider"></div>
<div class="abs city" style="top:2700px">Oakvale, AZ</div>
<div class="abs city" style="top:2732px">Brinmoor, WI</div>
<div class="abs city" style="top:2764px">Larkton, CO</div>
<div class="abs city" style="top:2796px">Fenwick City, KS / MO</div>
<div class="abs city-phone" style="top:2700px"><svg width="16" height="16" viewBox="0 0 24 24"><path fill="#fff" d="M6.6 10.8a15.1 15.1 0 0 0 6.6 6.6l2.2-2.2c.3-.3.7-.4 1-.2 1.1.4 2.3.6 3.6.6.6 0 1 .4 1 1V20c0 .6-.4 1-1 1A17 17 0 0 1 3 4c0-.6.4-1 1-1h3.5c.6 0 1 .4 1 1 0 1.3.2 2.5.6 3.6.1.3 0 .7-.2 1z"/></svg>123 456 7890</div>
<div class="abs city-phone" style="top:2732px"><svg width="16" height="16" viewBox="0 0 24 24"><path fill="#fff" d="M6.6 10.8a15.1 15.1 0 0 0 6.6 6.6l2.2-2.2c.3-.3.7-.4 1-.2 1.1.4 2.3.6 3.6.6.6 0 1 .4 1 1V20c0 .6-.4 1-1 1A17 17 0 0 1 3 4c0-.6.4-1 1-1h3.5c.6 0 1 .4 1 1 0 1.3.2 2.5.6 3.6.1.3 0 .7-.2 1z"/></svg>123 456 7890</div>
<div class="abs city-phone" style="top:2764px"><svg width="16" height="16" viewBox="0 0 24 24"><path fill="#fff" d="M6.6 10.8a15.1 15.1 0 0 0 6.6 6.6l2.2-2.2c.3-.3.7-.4 1-.2 1.1.4 2.3.6 3.6.6.6 0 1 .4 1 1V20c0 .6-.4 1-1 1A17 17 0 0 1 3 4c0-.6.4-1 1-1h3.5c.6 0 1 .4 1 1 0 1.3.2 2.5.6 3.6.1.3 0 .7-.2 1z"/></svg>123 456 7890</div>
<div class="abs city-phone" style="top:2796px"><svg width="16" height="16" viewBox="0 0 24 24"><path fill="#fff" d="M6.6 10.8a15.1 15.1 0 0 0 6.6 6.6l2.2-2.2c.3-.3.7-.4 1-.2 1.1.4 2.3.6 3.6.6.6 0 1 .4 1 1V20c0 .6-.4 1-1 1A17 17 0 0 1 3 4c0-.6.4-1 1-1h3.5c.6 0 1 .4 1 1 0 1.3.2 2.5.6 3.6.1.3 0 .7-.2 1z"/></svg>123 456 7890</div>

<div class="abs foot-heading" style="left:648px">Get in touch with us</div>
<div class="abs field" style="left:650px;top:2688px;width:226px;height:36px">Enter Name</div>
<div class="abs field" style="left:888px;top:2688px;width:228px;height:36px">Enter Contact No.</div>
<div class="abs field" style="left:650px;top:2734px;width:466px;height:36px">Enter Email Id</div>
<div class="abs field" style="left:650px;top:2780px;width:466px;height:82px">Enter Message</div>
<div class="abs submit">SUBMIT</div>

<footer class="abs copyright">©&nbsp;<b>BRIGHT ARROW EXPRESS DELIVERY</b>&nbsp;- 2016. All Rights Reserved.</footer>

</body>
</html>
```